Vantrelix Template Refresh 2017

We want software development managers to remember that presentations using this template showcased Vantrelix technology: Our template must be distinctive to be remembered as showing Vantrelix technology: They must stand out from the 100s of other tech presentations they see, without being 'wacky', but professional whether bold or subtle. We are targeting the world's largest corporations.

[What do we do?] Vantrelix offers the world's first objective, fair measure of software developer productivity (Vantrelix Keystroke Gauge) and code quality (Vantrelix DUX) metrics.

Our corporate colour is (hex) Red: 13, Green: 10, Blue: 74.

Target Market(s)

CIOs, CTOs and senior software development managers in large Enterprises.

Industry/Entity Type

Information Technology

Font styles to use
Sans Serif

Colors
0355a3

Requirements
Must have
• A memorable design
Nice to have
• Template for slides that will show a view of our User Interface (which shows graphs and charts); ideally a consistent theme to make it clear that this is our own UI, not general graphs and charts to illustrate the presentation. (None of the graphs and charts in the attached presentation are from our User Interface)
• A suggestion would be to make use of our "chord" shape (cut off circle in our logo). This could be white on a blue to appear as a cut-out window for the slide content.
Should not have
• A colourful / jokey / fun tone.

```html
<!DOCTYPE html>
<html lang="en">
<head>
<meta charset="utf-8">
<title>Example Source Code Metrics – Vantrelix</title>
<link rel="stylesheet" href="https://fonts.googleapis.com/css2?family=Russo+One&family=PT+Sans:wght@400;700&family=Carlito:wght@400;700&display=swap">
<style>
  :root {
    --navy: #22204f;
    --navy-deep: #0d0a4a;
    --white: #ffffff;
    --ink: #2b2b3a;
    --frame: #3a3a3f;
    --frame-edge: #2c2c30;
    --base: #d9d9db;
    --base-shadow: #bdbdc1;
    --row-dark: #95aed6;
    --row-light: #c8d6ea;
    --row-line: #ffffff;
    --rule: #d0d0d6;
    --footer: #6d6d70;
    --footer-line: #8a8a8e;
  }
  * { box-sizing: border-box; margin: 0; padding: 0; }
  html, body { width: 1200px; height: 900px; overflow: hidden; background: var(--white); }
  .slide { position: relative; width: 1200px; height: 900px; background: var(--white); font-family: "PT Sans", sans-serif; color: var(--ink); }

  .header { position: absolute; left: 0; top: 0; width: 1200px; height: 80px; background: var(--navy); display: flex; align-items: center; justify-content: space-between; padding: 0 24px 0 22px; }
  .header__title { font-family: "Russo One", sans-serif; font-weight: 400; font-size: 34px; color: var(--white); letter-spacing: 1px; }
  .brand { display: flex; align-items: center; gap: 10px; color: var(--white); font-weight: 700; font-size: 34px; }
  .brand__dot { width: 26px; height: 26px; border-radius: 50%; background: var(--white); }
  .header-rule { position: absolute; left: 0; top: 84px; width: 1200px; height: 3px; background: var(--rule); }

  .intro { position: absolute; left: 82px; top: 126px; width: 1080px; display: flex; gap: 26px; }
  .intro__marker { flex: none; width: 14px; height: 14px; margin: 10px 0 0 12px; border-radius: 50%; background: var(--navy-deep); }
  .intro__text { font-size: 21.5px; line-height: 33px; color: var(--ink); }

  .frame { position: absolute; left: 82px; top: 210px; width: 1028px; height: 580px; background: var(--frame); border: 2px solid var(--frame-edge); border-radius: 26px 26px 0 0; }
  .screen { position: absolute; left: 102px; top: 237px; width: 988px; height: 543px; overflow: hidden; background: var(--row-light); }
  .base { position: absolute; left: 52px; top: 780px; width: 1096px; height: 38px; background: var(--base); border-radius: 4px 4px 14px 14px; border-bottom: 6px solid var(--base-shadow); }

  .metrics { list-style: none; font-family: "Carlito", sans-serif; font-size: 14px; line-height: 18px; color: #1a1a24; }
  .metrics__row { display: grid; grid-template-columns: 276px 1fr; height: 63px; overflow: hidden; border-bottom: 1px solid var(--row-line); }
  .metrics__row:first-child { height: 75px; }
  .metrics__row:nth-child(odd) { background: var(--row-dark); }
  .metrics__row:nth-child(even) { background: var(--row-light); }
  .metrics__name, .metrics__desc { padding: 9px 8px 0; }
  .metrics__row:first-child .metrics__name, .metrics__row:first-child .metrics__desc { padding-top: 20px; }
  .metrics__name { border-right: 1px solid var(--row-line); }

  .footer-rule { position: absolute; left: 0; top: 847px; width: 1200px; height: 2px; background: var(--footer-line); }
  .footer { position: absolute; left: 0; top: 853px; width: 1200px; height: 47px; background: var(--footer); display: flex; align-items: center; justify-content: center; color: var(--white); font-weight: 700; font-size: 15px; letter-spacing: 0.6px; }
</style>
</head>
<body>
<div class="slide">
  <header class="header">
    <h1 class="header__title">EXAMPLE SOURCE CODE METRICS</h1>
    <div class="brand"><span class="brand__dot"></span><span>Vantrelix</span></div>
  </header>
  <div class="header-rule"></div>

  <div class="intro">
    <span class="intro__marker"></span>
    <p class="intro__text">Examples of the types of static source code metrics that are gathered from every interaction that every developer has with source files.</p>
  </div>

  <div class="frame"></div>
  <div class="screen">
    <ul class="metrics">
      <li class="metrics__row"><div class="metrics__name">Developer Interactions</div><div class="metrics__desc">Number of interactions by the programmer with the source code file in any given day.</div></li>
      <li class="metrics__row"><div class="metrics__name">Developer (Source) Lines of Code Flux</div><div class="metrics__desc">Sum the total lines of code added to or removed from the file by the programmer in any given day. In the case of source language files this is the sum the total source lines of code added to or removed from the file by the programmer in any given day. For Source Files this is in actual number of Source Lines Added + Removed.</div></li>
      <li class="metrics__row"><div class="metrics__name">Commit Comment Character Count</div><div class="metrics__desc">Extent of explanatory documentation contributed at the point of commit by the developer through period P</div></li>
      <li class="metrics__row"><div class="metrics__name">Developer Cyclomatic (Marrow) Flux</div><div class="metrics__desc">Sum Cyclomatic complexity added to or removed from the file by the programmer in any given day</div></li>
      <li class="metrics__row"><div class="metrics__name">Developer Hollingford Flux</div><div class="metrics__desc">Sum Hollingford complexity added to or removed from the file by the programmer in any given day</div></li>
      <li class="metrics__row"><div class="metrics__name">Developer Comment Lines of Code Flux</div><div class="metrics__desc">The number of comment characters added to or removed by the developer</div></li>
      <li class="metrics__row"><div class="metrics__name">Developer Filesize Flux</div><div class="metrics__desc">The filesize (in bytes) that the developer has added or removed from the source file</div></li>
      <li class="metrics__row"><div class="metrics__name">Number of Methods (NoM) Flux</div><div class="metrics__desc">Change in the Number of Methods (NoM) which is a change in an abstract, virtual or non-virtual method, a method declared in an interface, a constructor, a class constructor, a finalizer, a property/indexer getter or setter, an event adder or remover.</div></li>
      <li class="metrics__row"><div class="metrics__name">Depth of Inheritance (DIT) Flux</div><div class="metrics__desc">Change in Depth of Inheritance (DIT), which is the number of ancestor classes of a given class.</div></li>
    </ul>
  </div>
  <div class="base"></div>

  <div class="footer-rule"></div>
  <footer class="footer">COPYRIGHT © VANTRELIX LIMITED 2005-2016. ALL RIGHTS RESERVED</footer>
</div>
</body>
</html>
```